Ravelto Genova - handcrafted jeans and jeans textile accessories

design a new ecommerce website for a new jeans brand, handcrafted in Genova, the city were jeans were created more than 500 years ago. Jeans were used by port workers, now we are launching a new jeans collections with the same story ij the same place where they were created. The website is already in draft in shopify at the www.ravelto.it address, and the password for early access is "ventolupi"

I'd like to get -accessible luxury design -desktop home with fixed top menu -mobile home with hamburger menu or bottom menu -inspirational websites I'd like to look like: https://shop.fiorandoseldi.com/it-it/ https://it.cormatti.com/ -I already made a draft by myself on shopify: www.ravelto.it early access---> password: ventolupi -main color has to be the blue #0E2751 -accent colours should be similar to #a1711d and/or #a12f1d

Target Market(s)

accessible luxury market - high price

Industry/Entity Type

clothing, jeans

Number of Pages Required

4 page

Font styles to use
Other font styles liked:
• Quattrocento, Avenir

Colors
0054AA
0677BA
7BADD7
CADEEF
E8F1F8

Requirements
Must have
• fixed top menu, center logo, full width, blue color like #0E2751, home page video, press banner, top discount banner,
Nice to have
• mobile first design, google core vitals friendly

```html
<!DOCTYPE html>
<html lang="en">
<head>
<meta charset="utf-8">
<title>Ravelto Genova – The History of Jeans</title>
<link href="https://fonts.googleapis.com/css2?family=Quattrocento:wght@400;700&family=Nunito+Sans:ital,wght@0,400;0,600;0,700;1,400&display=swap" rel="stylesheet">
<style>
:root{
  --navy:#0E2751;
  --footer:#0c2552;
  --promo:#0054AA;
  --accent-blue:#0677BA;
  --text:#3a3a3a;
  --white:#ffffff;
  --rule:#6b6b6b;
}
*{margin:0;padding:0;box-sizing:border-box}
html,body{width:1200px;height:2223px;overflow:hidden;background:var(--white)}
body{font-family:'Nunito Sans',sans-serif;color:var(--text);position:relative}
.promo-bar{position:absolute;top:0;left:0;width:1200px;height:38px;background:var(--promo);color:var(--white);display:flex;align-items:center;justify-content:center;gap:8px;font-size:13.5px;font-weight:700;letter-spacing:.2px}
.hero{position:absolute;top:38px;left:0;width:1200px;height:625px;background:linear-gradient(180deg,#b86e68 0%,#c47a72 40%,#b59a8e 58%,#9c8c82 80%,#6e645e 100%)}
.utility-bar{position:absolute;top:38px;left:0;width:1200px;height:34px;background:rgba(60,50,50,.45);color:var(--white);font-size:12.5px;font-style:italic}
.utility-bar .left{position:absolute;left:100px;top:9px}
.utility-bar .right{position:absolute;right:102px;top:9px;display:flex;gap:8px;align-items:center}
.brand-name{font-family:'Quattrocento',serif;font-weight:400;color:var(--white);white-space:nowrap}
.header-brand{position:absolute;top:84px;left:0;width:1200px;text-align:center;font-size:28px;line-height:32px}
.main-nav{position:absolute;top:138px;left:422px;display:flex;gap:52px;color:var(--white);font-size:15.5px}
.nav-icons{position:absolute;top:133px;right:100px;display:flex;gap:12px}
.cart-count{position:absolute;right:-4px;bottom:-2px;width:15px;height:15px;border-radius:50%;background:var(--accent-blue);color:#fff;font-size:10px;display:flex;align-items:center;justify-content:center}
.hero-title{position:absolute;top:555px;left:0;width:1200px;text-align:center;font-family:'Quattrocento',serif;font-weight:700;font-size:53px;color:var(--white);letter-spacing:.5px}
.intro{position:absolute;top:726px;left:270px;width:660px;text-align:center;font-style:italic;font-size:15.5px;line-height:26px}
.story{position:absolute;top:868px;left:99px;width:475px;font-style:italic;font-size:15.5px;line-height:25.7px}
.story p{margin-bottom:25px}
.story-photo{position:absolute;top:868px;left:633px;width:469px;height:508px;background:linear-gradient(160deg,#6d6a5c 0%,#4a4a48 35%,#37436a 65%,#2d3a60 100%)}
.newsletter{position:absolute;top:1490px;left:0;width:1200px;text-align:center}
.newsletter h2{font-family:'Quattrocento',serif;font-weight:700;font-size:29px;color:var(--navy);letter-spacing:.5px}
.newsletter .underline{width:58px;height:2px;background:var(--promo);margin:6px auto 0}
.newsletter .lead{font-size:15.5px;line-height:26px;margin:24px auto 0;width:620px;color:#333}
.email-field{position:absolute;top:1645px;left:321px;width:558px;height:42px;border-bottom:1px solid var(--rule);font-style:italic;font-size:15.5px;color:#555}
.email-field span{position:absolute;left:5px;top:12px}
.email-field svg{position:absolute;right:4px;top:12px}
.consent{position:absolute;top:1703px;left:0;width:1200px;text-align:center;font-size:9px;color:#444}
.site-footer{position:absolute;top:1810px;left:0;width:1200px;height:343px;background:var(--footer);color:var(--white)}
.footer-col{position:absolute;top:55px}
.footer-col h3{font-family:'Quattrocento',serif;font-weight:700;font-size:16px;letter-spacing:.3px;margin-bottom:6px}
.footer-col p{font-size:13px;line-height:22.5px}
.footer-col li{list-style:none;font-size:13.5px;line-height:27px}
.footer-brand{position:absolute;top:70px;left:905px;width:210px;text-align:center;font-size:28px;line-height:32px}
.socials{position:absolute;top:128px;left:936px;display:flex;gap:11px}
.socials span{width:45px;height:45px;border:1.5px solid var(--white);border-radius:50%;display:block}
.payments{position:absolute;top:287px;left:483px;display:flex;gap:12px}
.payments span{width:40px;height:28px;border:2px solid #5a7aa8;border-radius:5px;display:block}
.bottom-bar{position:absolute;top:2153px;left:0;width:1200px;height:70px;background:var(--footer);border-top:1px solid #1a3466;color:var(--white);text-align:center;font-size:13.5px;padding-top:25px}
.scroll-btn{position:absolute;top:2134px;left:1121px;width:47px;height:47px;border-radius:50%;background:var(--white);display:flex;align-items:center;justify-content:center;box-shadow:0 1px 4px rgba(0,0,0,.2)}
</style>
</head>
<body>
<div class="promo-bar">
  <svg width="20" height="14" viewBox="0 0 20 14" fill="#fff" aria-hidden="true"><rect x="0" y="1" width="12" height="9"/><path d="M12 4h4l3 3v3h-7z"/><circle cx="4" cy="11.5" r="2"/><circle cx="15" cy="11.5" r="2"/></svg>
  RAVELTO LAUNCH PROMO - 20% OFF! - FREE SHIPPING - FREE RETURNS
</div>

<section class="hero" role="img" aria-label="Hero photograph: a man and a woman in denim posing by a wooden table with a striped bag against a pink wall"></section>
<div class="utility-bar">
  <div class="left">Free Shipping And Returns &nbsp;|&nbsp; 30 Days To Think About It</div>
  <div class="right">
    <svg width="11" height="11" viewBox="0 0 12 12" aria-hidden="true"><circle cx="6" cy="6" r="5.5" fill="#fff"/></svg>
    <span>English ⌄</span><span>&nbsp;|&nbsp;</span><span>Orders at</span>
    <svg width="10" height="10" viewBox="0 0 10 10" fill="#fff" aria-hidden="true"><path d="M2 0l2 2-1 2c1 1 2 2 3 3l2-1 2 2-2 2C4 10 0 6 0 2z"/></svg>
    <span>+39 010 555 0100</span>
  </div>
</div>
<div class="header-brand brand-name">Ravelto Genova</div>
<nav class="main-nav"><span>Jeans</span><span>Bags</span><span>Scarf</span><span>The Artisans</span></nav>
<div class="nav-icons">
  <svg width="26" height="26" viewBox="0 0 26 26" fill="none" stroke="#fff" stroke-width="1.8" aria-label="Search"><circle cx="11" cy="11" r="9"/><path d="M18 18l7 7"/></svg>
  <svg width="26" height="26" viewBox="0 0 26 26" fill="none" stroke="#fff" stroke-width="1.8" aria-label="Account"><circle cx="13" cy="8" r="6"/><path d="M2 25c0-6 5-10 11-10s11 4 11 10"/></svg>
  <div style="position:relative;width:26px;height:26px">
    <svg width="24" height="26" viewBox="0 0 24 26" fill="none" stroke="#fff" stroke-width="1.8" aria-label="Cart"><rect x="2" y="8" width="20" height="17"/><path d="M7 8V5a5 5 0 0110 0v3"/></svg>
    <span class="cart-count">0</span>
  </div>
</div>
<h1 class="hero-title">THE HISTORY OF JEANS</h1>

<p class="intro">Once upon a time there was the camallo Nico Ratti who, tired of being dirty already at 8 in the morning, decided to try to dye his moleskin pants with the indigo that the docks of the port that he unloaded every day were full of.</p>

<div class="story">
  <p>Once upon a time there was the camallo Nico Ratti who, tired of being dirty already at 8 in the morning, decided to try to dye his moleskin pants with the indigo that the docks of the port that he unloaded every day were full of.</p>
  <p style="margin-top:35px">It was the 15th century, and the Genoese were an economic and maritime power. Nico Ratti was not an economic power, at that time the bankers were already in charge, but he bought moleskin trousers in Chieri, near Turin.</p>
  <p>That fabric, a mix of cotton and linen, was perfect for port work because it was cool but also tough. Do you know the life of a 1500's camallo? All day up and down between the docks and the ships loaded with crates to unload. They didn't just call them "longshoremen"!</p>
  <p>Then came the French, who at first called it "Toile de Gênes", hence the word Jeans. However, they soon changed their minds, claiming their origin and calling them "Denim", that is, "from Nimes".</p>
</div>
<div class="story-photo" role="img" aria-label="Photograph: a man in a striped shirt and a woman in a denim shirt with a red jacket in front of an old wooden door"></div>

<section class="newsletter">
  <h2>BECOME A RAVELTER!</h2>
  <div class="underline"></div>
  <p class="lead">Sign up for our newsletter and get € 10 off your first order. And then you can read the news and stories about Ravelto. We will entertain you.</p>
</section>
<div class="email-field"><span>Email Address</span>
  <svg width="22" height="18" viewBox="0 0 22 18" fill="none" stroke="#0677BA" stroke-width="1.8" aria-label="Submit"><path d="M1 9h19M12 1l8 8-8 8"/></svg>
</div>
<p class="consent">By clicking on "Go" you declare that you have read the privacy policy and consent to the processing of your data.</p>

<footer class="site-footer">
  <div class="footer-col" style="left:100px;width:275px">
    <h3>WE ARE HERE FOR YOU</h3>
    <p>Lorem ipsum dolor sit amet,ctetur adipiscing elit, sed do eiusmod temporcidunt ut labore et dolore magna aliqua.s ipsum suspendisse ultrices gravida.</p>
  </div>
  <div class="footer-col" style="left:468px">
    <h3>HELPING</h3>
    <ul><li>Doubts about the size</li><li>Shipping and returns</li><li>Tel: +39 010 555 0142</li><li>Email: ciao@ravelto.it</li><li>Privacy disclaimer !</li></ul>
  </div>
  <div class="footer-col" style="left:710px">
    <h3>INFORMATION</h3>
    <ul><li>Search</li><li>Become a Seller</li><li>Contact Us</li><li>Refund Policy</li><li>Shipping Policy</li><li>Privacy Policy</li><li>Terms of Service</li></ul>
  </div>
  <div class="footer-brand brand-name">Ravelto Genova</div>
  <div class="socials" aria-label="Social links"><span></span><span></span><span></span></div>
  <div class="payments" aria-label="Accepted payment methods"><span></span><span></span><span></span><span></span></div>
</footer>
<div class="bottom-bar">© 2021 Ravelto. Caruggi di Piero Valdrini Registered office via dei Velai 8 - 16100 Genoa - Italy VAT number IT00000000000. All rights reserved.</div>
<div class="scroll-btn"><svg width="18" height="10" viewBox="0 0 18 10" fill="none" stroke="#0E2751" stroke-width="1.5" aria-hidden="true"><path d="M1 1l8 8 8-8"/></svg></div>
</body>
</html>
```